Brindle Works - Fast, Efficient and Gas Mainteance for Domestic, Commercial and Industrial clients

We are in the process of purchasing a new business and would like to get a new logo and business card.
Business is a gas maintenance business that also does new gas installations.
Has been established since 1988.
Services include:
Install all types of gas appliances & equipment inc. hot water units
Maintain / repair / replace all types of gas appliances & equipment

Target Market(s)

Domestic, Commercial and Industrial clients

Industry/Entity Type

Business

Contact Information for Business Card

admin@brindleworks-example.com.au
07 5981 4726
Brindle Works PTY LTD

Logo Text

Gas Fitting & Plumbing Maintenance Specialists

Font styles to use
Sans Serif

Requirements
Must have
• Logo
• Business name, contact number, email address, web address
• Domestic | Commercial | Industrial Est Since 1988
Nice to have
• Possibly a black card with a flame logo to one side
Should not have
• Spelling errors

```html
<!DOCTYPE html>
<html lang="en">
<head>
<meta charset="utf-8">
<title>Brindle Works – Business Card</title>
<link rel="stylesheet" href="https://fonts.googleapis.com/css2?family=Questrial&family=PT+Sans:ital,wght@0,400;1,700&display=swap">
<style>
  :root {
    --card-black: #000000;
    --card-red: #ec2024;
    --brand-yellow: #f7d117;
    --brand-orange: #f47a20;
    --text-white: #ffffff;
    --page-bg: #ecebe8;
  }
  * { box-sizing: border-box; margin: 0; padding: 0; }
  html, body { width: 1200px; height: 900px; overflow: hidden; }
  body { background: var(--page-bg); position: relative; font-family: "PT Sans", sans-serif; }

  .card { position: absolute; overflow: hidden; box-shadow: 0 6px 18px rgba(0,0,0,.18); }

  /* Front card */
  .card-front { left: 78px; top: 34px; width: 588px; height: 364px; background: var(--card-red); }
  .front-header { position: absolute; left: 0; top: 0; width: 100%; height: 175px; background: var(--card-black); }
  .front-brand { position: absolute; left: 36px; top: 62px; display: flex; align-items: center; gap: 16px; }
  .brand-dot { width: 34px; height: 34px; border-radius: 50%; background: var(--brand-orange); }
  .brand-name-front { font-family: "Questrial", sans-serif; font-size: 50px; color: var(--brand-yellow); line-height: 1; }

  .front-details { position: absolute; left: 30px; top: 200px; color: var(--text-white); font-size: 16px; line-height: 24px; }
  .address { margin-bottom: 17px; }
  .contact-row { display: flex; align-items: center; gap: 10px; height: 24.5px; }
  .contact-row svg { width: 13px; height: 13px; fill: var(--text-white); flex: none; }

  /* Back card */
  .card-back { left: 388px; top: 505px; width: 567px; height: 352px; background: var(--card-black); }
  .back-smoke { position: absolute; inset: 0; background: radial-gradient(ellipse at 40% 20%, #1a1410 0%, transparent 45%), radial-gradient(ellipse at 45% 85%, #10180e 0%, transparent 45%), var(--card-black); }
  .back-band { position: absolute; left: 0; top: 95px; width: 100%; height: 163px; background: var(--card-red); text-align: center; color: var(--text-white); }
  .brand-name-back { font-family: "Questrial", sans-serif; font-size: 54px; line-height: 1; margin-top: 32px; }
  .tagline { font-style: italic; font-weight: 700; font-size: 16px; margin-top: 34px; }
</style>
</head>
<body>

  <section class="card card-front">
    <div class="front-header">
      <div class="front-brand">
        <span class="brand-dot"></span>
        <span class="brand-name-front">Brindle Works</span>
      </div>
    </div>
    <div class="front-details">
      <p class="address">12345, Address Goes Here<br>Country Name, 123456</p>
      <p class="contact-row">
        <svg viewBox="0 0 16 16"><path d="M3.6 1.2l2.2 2.6c.3.4.3 1-.1 1.3L4.6 6.2c.9 2 2.6 3.7 4.6 4.6l1.1-1.1c.3-.4.9-.4 1.3-.1l2.6 2.2c.4.3.4.9.1 1.3l-1.2 1.4c-.5.6-1.4.8-2.1.5C6.4 13.4 2.6 9.6 1 4.9.7 4.2.9 3.3 1.5 2.8l1.4-1.2c.2-.3.5-.4.7-.4z"/></svg>
        <span>07 5981 4726</span>
      </p>
      <p class="contact-row">
        <svg viewBox="0 0 16 16"><path d="M1 3h14v10H1z M2.5 4.5v.6L8 8.8l5.5-3.7v-.6z" fill-rule="evenodd"/></svg>
        <span>admin@brindleworks-example.com.au</span>
      </p>
      <p class="contact-row">
        <svg viewBox="0 0 16 16"><path d="M6.6 9.4a.9.9 0 0 1 0-1.3l1.5-1.5a.9.9 0 1 1 1.3 1.3L7.9 9.4a.9.9 0 0 1-1.3 0zM4.7 8.8L3.2 10.3a1.8 1.8 0 0 0 2.5 2.5l1.5-1.5 1.3 1.3L7 14.1a3.6 3.6 0 0 1-5.1-5.1l1.5-1.5zM11.3 7.2l1.5-1.5a1.8 1.8 0 0 0-2.5-2.5L8.8 4.7 7.5 3.4 9 1.9a3.6 3.6 0 0 1 5.1 5.1l-1.5 1.5z"/></svg>
        <span>www.brindleworks-example.com.au</span>
      </p>
    </div>
  </section>

  <section class="card card-back">
    <div class="back-smoke" role="img" aria-label="Faint wisps of smoke on a black background"></div>
    <div class="back-band">
      <p class="brand-name-back">Brindle Works</p>
      <p class="tagline">Domestic | Commercial | Industrial Est Since 1988</p>
    </div>
  </section>

</body>
</html>
```